Video production company website

VistaKeel Productions is a video and photography production company serving many Fortune 500 clients traveling to Hawaii and International Destinations. Our primary focus is the Corporate and Incentive group market, and offer both photography and video services. In addition, we also create custom marketing, sales, art, and real estate productions.

Target Market(s)

Corporate Incentive Travel Groups

Industry/Entity Type

Videography

Number of Pages Required

4 page

Requirements
Must have
• see doc with content. This will ultimately be needed to be a wordpress design so we can update ourselves.
Nice to have
• sleek design, professional, cutting edge, modern
Should not have
• too much Hawaii Feel, some ok but we do travel international

```html
<!DOCTYPE html>
<html lang="en">
<head>
<meta charset="utf-8">
<title>VistaKeel Productions</title>
<link href="https://fonts.googleapis.com/css2?family=Oswald:wght@400;500&family=Roboto:wght@400;500;700&display=swap" rel="stylesheet">
<style>
:root{
  --accent:#ea4a1c;
  --accent-dark:#d63d12;
  --ink:#222;
  --muted:#666;
  --soft-bg:#f4f4f4;
  --quote-bg:#f2f2f2;
  --footer-bg:#231f20;
  --footer-base:#1a1a1a;
  --white:#fff;
}
*{margin:0;padding:0;box-sizing:border-box}
html,body{width:686px;height:1200px;overflow:hidden;background:var(--white)}
body{position:relative;font-family:'Roboto',Arial,sans-serif;color:var(--ink)}
.abs{position:absolute}
/* header */
.site-header{position:absolute;left:0;top:0;width:686px;height:59px;background:var(--white)}
.brand{position:absolute;left:50px;top:16px}
.brand-name{font-family:'Roboto',sans-serif;font-weight:500;font-size:14px;line-height:17px;color:var(--ink)}
.brand-tag{font-family:'Roboto',sans-serif;font-size:8.5px;letter-spacing:1px;color:var(--muted);margin-top:2px}
.main-nav a{position:absolute;top:25px;font-size:8px;color:#333;text-decoration:none;white-space:nowrap}
.main-nav a.active{color:var(--accent)}
.search-icon{position:absolute;left:622px;top:22px}
/* hero */
.hero{position:absolute;left:0;top:59px;width:686px;height:314px;background:linear-gradient(135deg,#4c5a3e 0%,#7a6a55 35%,#8d7b6b 55%,#5b6a4a 80%,#3c4a35 100%)}
.hero-play{position:absolute;left:318px;top:116px}
.hero-arrow{position:absolute;top:162px}
.hero-title{position:absolute;left:0;width:686px;top:190px;text-align:center;font-family:'Oswald',sans-serif;font-size:33px;font-weight:400;color:var(--white);letter-spacing:-.5px;text-shadow:0 1px 3px rgba(0,0,0,.4)}
.hero-sub{position:absolute;left:0;width:686px;top:230px;text-align:center;font-family:'Oswald',sans-serif;font-size:12px;color:var(--white);text-shadow:0 1px 2px rgba(0,0,0,.5)}
/* sections */
.section{position:absolute;left:0;width:686px}
.photo-section{top:373px;height:253px;background:var(--soft-bg)}
.video-section{top:626px;height:270px;background:var(--white)}
.section-title{position:absolute;left:0;width:686px;text-align:center;font-size:18px;font-weight:400;color:var(--accent)}
.section-sub{position:absolute;left:0;width:686px;text-align:center;font-size:9px;color:var(--muted)}
.card{position:absolute;width:192px;height:124px;overflow:hidden}
.card-caption{position:absolute;left:0;bottom:0;width:100%;height:37px;background:rgba(40,40,40,.7);padding:7px 0 0 19px;color:var(--white)}
.card-caption h3{font-size:8.5px;font-weight:500;line-height:10px}
.card-caption p{font-size:6px;line-height:8px}
.video-label{position:absolute;left:0;width:100%;bottom:9px;text-align:center;font-size:8.5px;font-weight:500;color:var(--white)}
.card-play{position:absolute;left:81px;top:44px}
.btn{position:absolute;height:26px;width:76px;background:var(--accent);color:var(--white);font-size:8.5px;text-align:center;line-height:26px;border-bottom:2px solid var(--accent-dark)}
/* testimonials */
.testimonials{position:absolute;left:2px;top:896px;width:684px;height:136px;background:var(--quote-bg)}
.avatar{position:absolute;width:54px;height:54px;border-radius:50%;background:radial-gradient(circle at 50% 40%,#d9a98a,#8d6a58 70%,#5a4a40)}
.quote{position:absolute;width:180px;font-size:6.5px;line-height:13px;color:#444}
.quote-mark{position:absolute;font-family:Georgia,serif;font-size:12px;color:#999}
.person-name{position:absolute;font-size:6px;font-weight:700;color:var(--accent)}
.person-role{position:absolute;font-size:6.5px;color:#555}
/* footer */
.site-footer{position:absolute;left:0;top:1032px;width:686px;height:129px;background:var(--footer-bg);border-top:3px solid #555}
.footer-title{position:absolute;font-size:8.5px;color:var(--white)}
.field{position:absolute;height:16px;background:var(--white);font-size:5.5px;color:#333;padding:5px 0 0 3px}
.send-btn{position:absolute;left:50px;top:99px;width:48px;height:16px;background:var(--accent);color:var(--white);font-size:6px;text-align:center;line-height:16px}
.footer-text{position:absolute;font-size:6px;color:#ddd;line-height:14px}
.footer-links li{list-style:none;font-size:6px;color:#ddd;line-height:14px}
.footer-links li::before{content:"";display:inline-block;border-left:3px solid #ddd;border-top:2.5px solid transparent;border-bottom:2.5px solid transparent;margin-right:4px}
.social{position:absolute;top:86px;width:20px;height:20px;border:1px solid #ccc;border-radius:50%}
.footer-base{position:absolute;left:0;top:1161px;width:686px;height:39px;background:var(--footer-base)}
.copyright{position:absolute;left:0;width:686px;top:14px;text-align:center;font-size:6.5px;color:var(--white)}
</style>
</head>
<body>

<header class="site-header">
  <div class="brand">
    <div class="brand-name">VistaKeel Productions</div>
    <div class="brand-tag">Stories Worth Keeping</div>
  </div>
  <nav class="main-nav">
    <a class="active" style="left:244px">HOME</a>
    <a style="left:287px">ABOUT</a>
    <a style="left:333px">PHOTOGRAPHER</a>
    <a style="left:414px">VIDEO PRODUCTION</a>
    <a style="left:506px">GALLERIES</a>
    <a style="left:567px">CONTACTS</a>
  </nav>
  <svg class="search-icon" width="13" height="13" viewBox="0 0 13 13"><circle cx="5.2" cy="5.2" r="4" fill="none" stroke="#444" stroke-width="1.8"/><line x1="8.2" y1="8.2" x2="12" y2="12" stroke="#444" stroke-width="2"/></svg>
</header>

<section class="hero" role="img" aria-label="Family in floral leis at an evening garden party in a resort lawn">
  <svg class="hero-play" width="50" height="50" viewBox="0 0 50 50"><circle cx="25" cy="25" r="23" fill="rgba(0,0,0,.45)" stroke="rgba(255,255,255,.7)" stroke-width="2"/><polygon points="19,14 36,25 19,36" fill="#fff"/></svg>
  <svg class="hero-arrow" style="left:38px" width="16" height="16" viewBox="0 0 16 16"><circle cx="8" cy="8" r="8" fill="rgba(0,0,0,.55)"/><polyline points="9.5,4.5 6,8 9.5,11.5" fill="none" stroke="#fff" stroke-width="1.5"/></svg>
  <svg class="hero-arrow" style="left:630px" width="16" height="16" viewBox="0 0 16 16"><circle cx="8" cy="8" r="8" fill="rgba(0,0,0,.55)"/><polyline points="6.5,4.5 10,8 6.5,11.5" fill="none" stroke="#fff" stroke-width="1.5"/></svg>
  <h1 class="hero-title">VISTAKEEL PRODUCTIONS</h1>
  <p class="hero-sub">Neque porro quisquam est qui dolorem ipsum quia dolor sit amet</p>
</section>

<section class="section photo-section">
  <h2 class="section-title" style="top:26px">PHOTOGRAPHY</h2>
  <p class="section-sub" style="top:53px">Neque porro quisquam est qui dolorem ipsum quia dolor sit amet</p>
  <div class="card" style="left:50px;top:79px;background:linear-gradient(160deg,#8fb0c8,#6d8a5a 55%,#3c4a30)" role="img" aria-label="Golf group holding clubs on a course">
    <div class="card-caption"><h3>PHOTOGRAPHY</h3><p>Neque porro quisquam est qui dolorem</p></div>
  </div>
  <div class="card" style="left:247px;top:79px;background:linear-gradient(180deg,#e0a83a,#c9782a 50%,#5b6a3a)" role="img" aria-label="Couple with leis at sunset on the beach">
    <div class="card-caption"><h3>PHOTOGRAPHY</h3><p>Neque porro quisquam est qui</p></div>
  </div>
  <div class="card" style="left:444px;top:79px;background:linear-gradient(180deg,#2a1a14,#6b3a2a 50%,#2a1a14)" role="img" aria-label="Guests posing at a night event with lit sign">
    <div class="card-caption"><h3>PHOTOGRAPHY</h3><p>Neque porro quisquam est</p></div>
  </div>
  <div class="btn" style="left:301px;top:216px">VIEW MORE</div>
</section>

<section class="section video-section">
  <h2 class="section-title" style="top:28px">VIDEO PRODUCTION</h2>
  <p class="section-sub" style="top:54px">Neque porro quisquam est qui dolorem ipsum quia dolor sit amet</p>
  <div class="card" style="left:52px;top:78px;background:linear-gradient(150deg,#3a2418,#8a4a2a 50%,#1c120c)" role="img" aria-label="Polynesian dancers performing at night">
    <svg class="card-play" width="30" height="30" viewBox="0 0 30 30"><circle cx="15" cy="15" r="14" fill="rgba(0,0,0,.45)" stroke="rgba(255,255,255,.7)" stroke-width="1.5"/><polygon points="11,8 22,15 11,22" fill="#fff"/></svg>
    <div class="video-label">VIDEO PRODUCTION</div>
  </div>
  <div class="card" style="left:249px;top:78px;background:radial-gradient(circle at 50% 30%,#7a6a70,#1a1a22 60%,#0c0c12)" role="img" aria-label="Fireworks over the sea at night">
    <svg class="card-play" width="30" height="30" viewBox="0 0 30 30"><circle cx="15" cy="15" r="14" fill="rgba(0,0,0,.45)" stroke="rgba(255,255,255,.7)" stroke-width="1.5"/><polygon points="11,8 22,15 11,22" fill="#fff"/></svg>
    <div class="video-label">VIDEO PRODUCTION</div>
  </div>
  <div class="card" style="left:445px;top:78px;background:linear-gradient(160deg,#5a4aa0,#7a3a8a 45%,#2a1a3a)" role="img" aria-label="Evening party with stage lights and guests">
    <svg class="card-play" width="30" height="30" viewBox="0 0 30 30"><circle cx="15" cy="15" r="14" fill="rgba(0,0,0,.45)" stroke="rgba(255,255,255,.7)" stroke-width="1.5"/><polygon points="11,8 22,15 11,22" fill="#fff"/></svg>
    <div class="video-label" style="bottom:12px">VIDEO PRODUCTION</div>
  </div>
  <div class="btn" style="left:305px;top:217px">VIEW MORE</div>
</section>

<section class="testimonials">
  <svg class="abs" style="left:34px;top:58px" width="12" height="22" viewBox="0 0 12 22"><polyline points="11,1 1,11 11,21" fill="none" stroke="#aaa" stroke-width="1"/></svg>
  <svg class="abs" style="left:636px;top:58px" width="12" height="22" viewBox="0 0 12 22"><polyline points="1,1 11,11 1,21" fill="none" stroke="#aaa" stroke-width="1"/></svg>

  <div class="avatar" style="left:59px;top:35px" role="img" aria-label="Portrait of a client"></div>
  <span class="quote-mark" style="left:125px;top:40px">&ldquo;</span>
  <p class="quote" style="left:134px;top:45px">Lorem Ipsum has been the industry's standard dummy text ever since the 1500s, when an unknown printer took a galley of type and scrambled it to make</p>
  <span class="quote-mark" style="left:283px;top:73px">&rdquo;</span>
  <span class="person-name" style="left:134px;top:90px">OWEN HARTLEY</span>
  <span class="person-role" style="left:134px;top:102px">Owner and Producer</span>

  <div class="avatar" style="left:374px;top:35px" role="img" aria-label="Portrait of a client"></div>
  <span class="quote-mark" style="left:441px;top:40px">&ldquo;</span>
  <p class="quote" style="left:450px;top:45px">Lorem Ipsum has been the industry's standard dummy text ever since the 1500s, when an unknown printer took a galley of type and scrambled it to make</p>
  <span class="quote-mark" style="left:605px;top:73px">&rdquo;</span>
  <span class="person-name" style="left:450px;top:90px">MARCUS LIND</span>
  <span class="person-role" style="left:450px;top:102px">Producer</span>
</section>

<footer class="site-footer">
  <h4 class="footer-title" style="left:50px;top:27px;font-weight:400">CONTACT FORM</h4>
  <div class="field" style="left:51px;top:42px;width:75px">Name</div>
  <div class="field" style="left:129px;top:42px;width:75px">Company info</div>
  <div class="field" style="left:51px;top:61px;width:75px">Phone</div>
  <div class="field" style="left:129px;top:61px;width:75px">Email</div>
  <div class="field" style="left:51px;top:79px;width:153px">Message</div>
  <div class="send-btn">SEND</div>

  <h4 class="footer-title" style="left:262px;top:24px;font-weight:400">LINKS</h4>
  <ul class="footer-links abs" style="left:262px;top:43px">
    <li>About</li><li>Photographer</li><li>Featured</li><li>Galleries</li>
  </ul>

  <h4 class="footer-title" style="left:380px;top:24px;font-weight:400">GET IN TOUCH</h4>
  <p class="footer-text" style="left:381px;top:43px;line-height:12px">VistaKeel Productions, LLC<br>P.O. Box 210-557<br>Westbay HI 96700<br>Phone : (808) 555.0142<br>Fax : (808) 555.0187</p>

  <h4 class="footer-title" style="left:517px;top:24px;font-weight:400">NEWSLETTER</h4>
  <p class="footer-text" style="left:517px;top:43px;width:120px;line-height:10px">Your about us information would fit here nicely.</p>
  <div class="field" style="left:517px;top:68px;width:80px;height:17px;color:#777;padding-left:8px">Email address</div>
  <div class="abs" style="left:597px;top:68px;width:36px;height:17px;background:var(--accent);color:#fff;font-size:6px;text-align:center;line-height:17px">Submit</div>
  <div class="social" style="left:517px"></div>
  <div class="social" style="left:544px"></div>
  <div class="social" style="left:572px"></div>
</footer>

<div class="footer-base">
  <p class="copyright">Copyright &copy; 2016. All Rights Reserved</p>
</div>

</body>
</html>
```